We need a modern Google Slides/ PowerPoint presentation for our business brokerage firm in California. Please see attached design colors for colors and fonts- primary colors: white, blue & yellow. On the cover slide we want our logo to be white on blue background (I do not have our logo in white yet, so you can just leave place for logo.) Please limit the amount of stock photos with people. We will insert "Team" photos ourselves, just leave a place for them. Content is attached. Thank you!

```html
<!DOCTYPE html>
<html lang="en">
<head>
<meta charset="utf-8">
<title>Crestline Business Advisors – Slide Deck</title>
<link href="https://fonts.googleapis.com/css2?family=Poppins:wght@700;800&family=Open+Sans:wght@400;600&family=Roboto:wght@400;700&display=swap" rel="stylesheet">
<style>
:root{
  --stage:#7a7879;
  --navy:#0f2150;
  --navy-deep:#0b1a3f;
  --yellow:#fff200;
  --white:#ffffff;
  --ink:#1c1c1c;
  --grey-text:#8a8a8a;
  --light-bg:#dcdcdc;
  --red:#c8000f;
  --green:#6bb43c;
  --sky:#19b3ff;
}
*{margin:0;padding:0;box-sizing:border-box}
html,body{width:1200px;height:1037px;overflow:hidden;background:var(--stage)}
body{position:relative;font-family:"Open Sans",sans-serif}
.slide{position:absolute;width:523px;height:294px;overflow:hidden;box-shadow:0 2px 8px rgba(0,0,0,.25)}
.col-a{left:66px}.col-b{left:610px}
.row-1{top:57px}.row-2{top:371px}.row-3{top:685px}
.heading{font-family:"Poppins",sans-serif;font-weight:800;letter-spacing:-.2px;line-height:1.3}
.brand{position:absolute;font-family:"Open Sans",sans-serif;font-weight:600;line-height:1;color:var(--navy)}
.brand .name{display:block;font-size:13px;letter-spacing:1.5px}
.brand .sub{display:block;font-size:5px;letter-spacing:1.2px;margin-top:2px}
.brand.light{color:var(--white)}
.photo{position:absolute}

/* Cover */
.cover{background:var(--navy)}
.cover .photo{inset:0 0 39px 0;background:linear-gradient(180deg,#142b63 0%,#1a3570 40%,#0f2150 100%)}
.cover .brand{left:27px;top:52px}
.cover .brand .name{font-size:25px;letter-spacing:3px}
.cover .brand .sub{font-size:9.5px;letter-spacing:2px;margin-top:3px}
.cover .headline{position:absolute;left:27px;top:118px;color:var(--yellow);font-size:21.5px}
.cover .lead{position:absolute;left:27px;top:158px;width:470px;color:var(--white);font-size:14.5px;line-height:20.5px}
.cover .footer{position:absolute;left:0;bottom:0;width:100%;height:39px;background:var(--yellow);color:var(--ink);font-size:9.6px;display:flex;align-items:center;justify-content:center;gap:5px}

/* Intro */
.intro{background:var(--white)}
.intro .photo{right:0;top:0;width:330px;height:100%;background:linear-gradient(90deg,rgba(255,255,255,1) 0%,#e6ebf1 25%,#9aa4b4 55%,#2a2f3c 85%,#141822 100%)}
.intro .brand{right:4px;top:13px}
.intro .headline{position:absolute;left:26px;top:26px;color:var(--navy);font-size:20.5px;line-height:27px}
.intro .hook{position:absolute;left:26px;top:120px;font-family:"Open Sans",sans-serif;font-weight:600;font-size:17px;color:var(--ink)}
.intro .tease{position:absolute;left:26px;top:144px;width:260px;font-size:17px;line-height:25px;color:var(--grey-text)}

/* Framework */
.framework{background:var(--white)}
.framework .headline{position:absolute;left:20px;top:14px;color:var(--navy);font-size:21px}
.framework .brand{right:21px;top:33px}
.framework .intro-line{position:absolute;left:20px;top:48px;width:320px;font-size:8px;line-height:11px;color:#777}
.steps{position:absolute;left:27px;top:91px;width:470px;display:grid;grid-template-columns:219px 219px;column-gap:0;row-gap:0}
.step{position:relative;height:65px;padding-left:30px}
.step .num{position:absolute;left:0;top:1px;width:24px;height:24px;border-radius:50%;font-family:"Roboto",sans-serif;font-weight:700;font-size:10px;display:flex;align-items:center;justify-content:center}
.step .num.dark{background:var(--navy);color:var(--white)}
.step .num.bright{background:var(--yellow);color:var(--ink)}
.step .title{font-family:"Roboto",sans-serif;font-weight:700;font-size:7.4px;color:var(--ink)}
.step .desc{margin-top:4px;width:148px;font-size:4.8px;line-height:6.4px;color:#666}

/* Fees */
.fees{background:var(--navy-deep)}
.fees .photo{right:0;top:0;width:300px;height:100%;background:radial-gradient(ellipse at 70% 55%,#2e6fa6 0%,#17406f 40%,#0d2147 75%,#0b1a3f 100%)}
.fees .brand{left:440px;top:80px}
.fees .headline{position:absolute;left:27px;top:54px;color:var(--white);font-size:21px;line-height:27px}
.fees .lead{position:absolute;left:27px;top:124px;width:300px;color:var(--white);font-size:13.4px;line-height:23.5px}

/* Services */
.services{background:var(--light-bg)}
.services .headline{position:absolute;left:20px;top:20px;color:var(--navy);font-size:21px}
.services .brand{right:21px;top:33px}
.cards{position:absolute;left:15px;top:75px;display:flex;gap:7px}
.card{width:118px;height:177px;color:var(--white);text-align:center;padding-top:14px}
.card.red{background:var(--red)}.card.green{background:var(--green)}.card.sky{background:var(--sky)}.card.navy{background:var(--navy)}
.card .icon{width:54px;height:54px;border-radius:50%;background:var(--white);margin:0 auto;display:flex;align-items:center;justify-content:center}
.card .title{margin-top:11px;font-family:"Roboto",sans-serif;font-weight:700;font-size:8.3px}
.card .desc{margin:9px auto 0;width:96px;font-family:"Roboto",sans-serif;font-size:5.2px;line-height:9.2px}

/* Preparation */
.prep{background:var(--navy)}
.prep .photo{inset:0}
.prep .brand{right:4px;top:13px}
.prep .headline{position:absolute;left:24px;top:54px;color:var(--white);font-size:21px}
.prep .lead{position:absolute;left:24px;top:98px;width:305px;color:var(--white);font-size:13.4px;line-height:23.5px}
</style>
</head>
<body>

<section class="slide cover col-a row-1">
  <div class="photo" role="img" aria-label="Night city skyline with bay bridge in deep blue tones"></div>
  <div class="brand light"><span class="name">CRESTLINE</span><span class="sub">BUSINESS ADVISORS</span></div>
  <h1 class="heading headline">WE SELL BUSINESSES MORE EFFECTIVELY</h1>
  <p class="lead">We are a full-service business brokerage &amp; M&amp;A advisory firm in California. With our proven strategic framework, we sell privately held businesses at a greater value and in less time</p>
  <div class="footer"><span>License Number : 1234656</span><span>|</span><span>Address : 123,Lorem ipsum doloronsectetur</span><span>|</span><span>Phone : 1 888 888 8888</span><span>|</span><span>Website</span></div>
</section>

<section class="slide intro col-b row-1">
  <div class="photo" role="img" aria-label="Two businessmen in suits talking at an office table with a laptop"></div>
  <div class="brand"><span class="name">CRESTLINE</span><span class="sub">BUSINESS ADVISORS</span></div>
  <h2 class="heading headline">TALKING TO OTHER<br>BUSINESS BROKERAGE<br>FIRMS?</h2>
  <p class="hook">Awesome, we encourage that.</p>
  <p class="tease">But here are a few things that make us different...</p>
</section>

<section class="slide framework col-a row-2">
  <h2 class="heading headline">OUR FRAMEWORK</h2>
  <div class="brand"><span class="name">CRESTLINE</span><span class="sub">BUSINESS ADVISORS</span></div>
  <p class="intro-line">We've helped hundreds of clients to sell their business at higher value by following our strategic framework.</p>
  <div class="steps">
    <div class="step"><span class="num dark">01</span><div class="title">Preparation &amp; Planning</div><p class="desc">This phase focuses on preparing your business for sale. We believe that advanced preparation is the key to success. It makes your business more attractive to potential buyers and allows you to get the best price for it.</p></div>
    <div class="step"><span class="num bright">02</span><div class="title">Business Valuation</div><p class="desc">We will advise you on the best method(s) to use to determine the price range for your business, help you gather the documents and understand the key factors that drive the value of your business. Business valuation takes into consideration the business's past, current financial statements and other factors.</p></div>
    <div class="step"><span class="num bright">03</span><div class="title">Marketing the Business</div><p class="desc">Once we've established the price and overall sales strategy, we will prepare a comprehensive marketing plan and begin promoting your business to qualified strategic buyers and business brokers. To maintain confidentiality, your business name and exact location will not be disclosed.</p></div>
    <div class="step"><span class="num dark">04</span><div class="title">Meet the buyer</div><p class="desc">A non-disclosure agreement must be signed by all interested buyers. Your business will be exposed to a wide range of buyers to generate competitive bids. We only work with buyers who meet the appropriate financial requirements to make the offer.</p></div>
    <div class="step"><span class="num dark">05</span><div class="title">Offers &amp; Negotiations</div><p class="desc">During this phase of the process, our goal is to produce the best possible offer for your business. We will assist you in evaluating each offer with our expertise on current market trends, financing matters and business law. With years of valuable negotiation experience and negotiation training, we will help you get the best possible price and terms for your business.</p></div>
    <div class="step"><span class="num bright">06</span><div class="title">Closing</div><p class="desc">We will work closely with your CPA, landlord, attorney, and all relevant third parties to ensure a smooth closing.</p></div>
  </div>
</section>

<section class="slide fees col-b row-2">
  <div class="photo" role="img" aria-label="Stacks of coins glowing blue under a rising stock candlestick chart"></div>
  <div class="brand light"><span class="name">CRESTLINE</span><span class="sub">BUSINESS ADVISORS</span></div>
  <h2 class="heading headline">WE DON’T CHARGE<br>UPFRONT COSTS</h2>
  <p class="lead">We are able to deliver world class business brokerage services without upfront costs for our clients. Our fees are success-based. With a success-based pricing model, our commission is earned AFTER the business is sold.</p>
</section>

<section class="slide services col-a row-3">
  <h2 class="heading headline">WHAT WE DO</h2>
  <div class="brand"><span class="name">CRESTLINE</span><span class="sub">BUSINESS ADVISORS</span></div>
  <div class="cards">
    <div class="card red">
      <div class="icon"><svg width="26" height="22" viewBox="0 0 26 22"><path d="M10 2H3v18h7" fill="none" stroke="#c8000f" stroke-width="3"/><path d="M9 8h7V3l9 8-9 8v-5H9z" fill="#c8000f"/></svg></div>
      <div class="title">Exit Planning</div>
      <p class="desc">Exit planning strategy will identify the actions that need to be taken so that you can exit your business with confidence.</p>
    </div>
    <div class="card green">
      <div class="icon"><svg width="28" height="22" viewBox="0 0 28 22"><rect x="1" y="5" width="4" height="12" fill="#6bb43c"/><rect x="23" y="5" width="4" height="12" fill="#6bb43c"/><path d="M6 7l6-3 4 2 6-1v9l-7 5-9-5z" fill="#6bb43c"/></svg></div>
      <div class="title">Business Valuations</div>
      <p class="desc">By utilizing a variety of valuation methods, we will evaluate your business and determine the most probable selling price.</p>
    </div>
    <div class="card sky">
      <div class="icon"><svg width="26" height="24" viewBox="0 0 26 24"><path d="M2 12L13 3l11 9h-3v10H5V12z" fill="#19b3ff"/><rect x="10" y="15" width="6" height="7" fill="#fff"/></svg></div>
      <div class="title">Seller Representation</div>
      <p class="desc">With our proven strategic framework, we'll help you to sell your business at a greater value and in less time</p>
    </div>
    <div class="card navy">
      <div class="icon"><svg width="24" height="24" viewBox="0 0 24 24"><circle cx="12" cy="12" r="10" fill="#0f2150"/><text x="12" y="16.5" text-anchor="middle" font-family="Roboto,sans-serif" font-weight="700" font-size="13" fill="#fff">$</text></svg></div>
      <div class="title">Buyer Representation</div>
      <p class="desc">From deal sourcing to closing, we guide business buyers through the entire process to set them up for success.</p>
    </div>
  </div>
</section>

<section class="slide prep col-b row-3">
  <svg class="photo" width="523" height="294" viewBox="0 0 523 294" role="img" aria-label="Business people reviewing documents and charts at a desk, shown behind a curved edge">
    <defs><linearGradient id="deskTone" x1="0" y1="0" x2="1" y2="1"><stop offset="0" stop-color="#3d5d8c"/><stop offset=".5" stop-color="#a9b8cc"/><stop offset="1" stop-color="#6f87a6"/></linearGradient></defs>
    <path d="M312 0H523V294H318C370 230 380 140 360 80 350 45 335 18 312 0Z" fill="url(#deskTone)"/>
  </svg>
  <div class="brand"><span class="name">CRESTLINE</span><span class="sub">BUSINESS ADVISORS</span></div>
  <h2 class="heading headline">PREPARATION &amp; PLANNING</h2>
  <p class="lead">Advanced preparation is the key to success. We help you to prepare your business for sale before it goes on the market. Exit planning strategy will make your business more attractive to the potential buyers and allow you to maximize the value of your business.</p>
</section>

</body>
</html>
```